The Lanternwork (a book about how to use the Freemasons tools in your everyday life)

This is a book about how to use in real life The ropes that Freemasons study in their allegories. It´s Freemasonry for people who are not initiated but they can use these metaphors about the square, the compass, the gavel, the level, etc in their life for becoming more productive and successful.

please note: this is not another book about freemasonry, or dedicated only to masons... it´s for mothers, workers, bus drivers, CEOs, students and professors. Everybody can take advantage in their lives of using this tools.

book covers to be considered:
Q-Doubled by Lia Brenhold
The ropes by Rudi Kemble
The weight of dawn by R Vashby

in the cover there must me this information:"How to use the philosophy of Freemasonry in your life" Added Thursday, April 16, 2015

Target Market(s)

people who read Delmont, Renato Vilhar, Ruvik.
people who likes books about Self Help
and of course, for freemasons also

Font styles to use
Serif

Requirements
Must have
• the title: The Lanternwork
• my name: Lorenzo Brisca
• additional information: "how to use the philosophy of Freemasonry in your everyday life"
Nice to have
• words like: Success, Motivation, etc
• masonic words like: Square, compass, gavel, level, etc

```html
<!DOCTYPE html>
<html lang="en">
<head>
<meta charset="utf-8">
<title>The Lanternwork — Lorenzo Brisca</title>
<link rel="stylesheet" href="https://fonts.googleapis.com/css2?family=Cormorant+Garamond:wght@400;500&family=Jost:wght@300;400&display=swap">
<style>
  :root {
    --page-bg: #f1f1f1;
    --cover-bg: #ffffff;
    --ink: #1a1a1a;
    --ink-soft: #4a4a4a;
    --rule: #d6d6d6;
    --square-accent: #b8862f;
    --compass-accent: #2f5d62;
    --level-accent: #7a3b52;
  }
  * { margin: 0; padding: 0; box-sizing: border-box; }
  html, body {
    width: 839px; height: 1200px; overflow: hidden;
    background: var(--page-bg);
  }
  .cover {
    position: absolute; left: 110px; top: 93px;
    width: 618px; height: 987px;
    background: var(--cover-bg);
    color: var(--ink);
    font-family: "Jost", "Futura", sans-serif;
  }
  .title {
    position: absolute; left: 0; right: 0; top: 176px;
    text-align: center;
    font-family: "Cormorant Garamond", Georgia, serif;
    font-weight: 400;
  }
  .title-the {
    display: block;
    font-size: 22px; letter-spacing: 12px; text-indent: 12px;
    color: var(--ink-soft);
  }
  .title-rule {
    display: block; width: 60px; height: 1px; margin: 12px auto 10px;
    background: var(--ink);
  }
  .title-main {
    display: block;
    font-size: 74px; line-height: 1; letter-spacing: 3px;
  }
  .tools {
    position: absolute; left: 44px; right: 44px; top: 362px;
    height: 146px;
    display: grid; grid-template-columns: repeat(3, 1fr);
  }
  .tool {
    display: flex; flex-direction: column; align-items: center; justify-content: center;
    gap: 10px; text-align: center;
  }
  .tool + .tool { border-left: 1px solid var(--rule); }
  .tool-mark { width: 28px; height: 28px; border: 2px solid currentColor; }
  .tool--square { color: var(--square-accent); }
  .tool--compass { color: var(--compass-accent); }
  .tool--compass .tool-mark { border-radius: 50%; }
  .tool--level { color: var(--level-accent); }
  .tool--level .tool-mark { height: 2px; border: 0; background: currentColor; width: 40px; margin: 13px 0; }
  .tool-name {
    font-family: "Cormorant Garamond", Georgia, serif;
    font-weight: 500; font-size: 22px; letter-spacing: 4px;
  }
  .tool-words {
    font-weight: 300; font-size: 15px; letter-spacing: 1px; line-height: 20px;
    color: var(--ink-soft);
  }
  .tagline {
    position: absolute; left: 0; right: 0; top: 553px;
    text-align: center; font-weight: 300; font-size: 26px; line-height: 33px;
  }
  .author {
    position: absolute; left: 0; right: 0; top: 728px;
    text-align: center; font-weight: 300; font-size: 64px; line-height: 1;
  }
</style>
</head>
<body>
  <main class="cover">
    <h1 class="title">
      <span class="title-the">THE</span>
      <span class="title-rule"></span>
      <span class="title-main">Lanternwork</span>
    </h1>
    <section class="tools">
      <div class="tool tool--square">
        <span class="tool-mark"></span>
        <span class="tool-name">SQUARE</span>
        <span class="tool-words">inspire<br>motivation</span>
      </div>
      <div class="tool tool--compass">
        <span class="tool-mark"></span>
        <span class="tool-name">COMPASS</span>
        <span class="tool-words">positive<br>fulfillment</span>
      </div>
      <div class="tool tool--level">
        <span class="tool-mark"></span>
        <span class="tool-name">LEVEL</span>
        <span class="tool-words">strive<br>success</span>
      </div>
    </section>
    <p class="tagline">"how to use the philosophy of<br>Freemasonry in your everyday life"</p>
    <p class="author">LORENZO BRISCA</p>
  </main>
</body>
</html>
```